Classy, Elegant, Simple Business Card Design

Looking to have a classy, simple, and elegant design. Want a top notch designed business card. I really like the look of the new brivo credit card. I also like the design I attached. I am trying to reach 21-29 year old females for booking us for there wedding or event. We offer Disc Jockey Service, Photo Booth Rentals, and Uplighting .

Target Market(s)

21-28 year old females

Contact Information for Business Card

Has to have logo, website, email, and phone number

Font styles to use
Other font styles liked:
• open to font choice, modern, clean
Designer to choose
33a6d7
0791cd
0555a3
ffffff

Requirements
Must have
• Has to have logo, website, email, and phone number
Nice to have
• I really like the design of the new brivo credit card. I also included my logo and some designs I like
Should not have
• clutter or too much info

```html
<!DOCTYPE html>
<html lang="en">
<head>
<meta charset="utf-8">
<title>Tidewell Event Group – Business Card</title>
<link rel="stylesheet" href="https://fonts.googleapis.com/css2?family=Jost:wght@400;500;600&display=swap">
<style>
  :root {
    --backdrop: #1d1f23;
    --card-deep: #0a2f5e;
    --card-base: #0d3c74;
    --pattern-tone: #134a8a;
    --accent-sky: #33a6d7;
    --accent-bright: #0791cd;
    --accent-royal: #0555a3;
    --ink-white: #ffffff;
    --ink-soft: #d9e6f3;
  }
  * { box-sizing: border-box; margin: 0; padding: 0; }
  html, body {
    width: 1200px;
    height: 900px;
    overflow: hidden;
    background: var(--backdrop);
    font-family: "Jost", "Helvetica Neue", Arial, sans-serif;
  }
  .sheet {
    position: relative;
    width: 1200px;
    height: 900px;
  }
  .card {
    position: absolute;
    left: 250px;
    width: 700px;
    height: 400px;
    border-radius: 6px;
    overflow: hidden;
    background: linear-gradient(135deg, var(--card-base) 0%, var(--card-deep) 100%);
    box-shadow: 0 18px 40px rgba(0, 0, 0, 0.45);
    color: var(--ink-white);
  }
  .card--front { top: 40px; }
  .card--back { top: 470px; }

  .pattern-field {
    position: absolute;
    display: block;
  }
  .card--front .pattern-field {
    right: -80px;
    bottom: -120px;
    width: 460px;
    height: 400px;
    border-radius: 50%;
    background: radial-gradient(ellipse at center, var(--pattern-tone) 0%, rgba(19, 74, 138, 0.35) 55%, rgba(19, 74, 138, 0) 72%);
  }
  .card--back .pattern-field {
    left: -110px;
    top: -40px;
    width: 340px;
    height: 480px;
    border-radius: 50%;
    background: radial-gradient(ellipse at center, var(--pattern-tone) 0%, rgba(19, 74, 138, 0.35) 55%, rgba(19, 74, 138, 0) 72%);
  }

  .brand {
    position: absolute;
    display: flex;
    align-items: center;
    gap: 14px;
  }
  .brand__dot {
    width: 22px;
    height: 22px;
    border-radius: 50%;
    background: var(--accent-sky);
    flex: none;
  }
  .brand__name {
    font-weight: 500;
    font-size: 34px;
    letter-spacing: 3px;
    color: var(--accent-sky);
    text-transform: uppercase;
    line-height: 1;
  }

  .card--front .brand {
    left: 0;
    right: 0;
    top: 150px;
    justify-content: center;
  }
  .front-url {
    position: absolute;
    left: 0;
    right: 0;
    top: 222px;
    text-align: center;
    font-size: 19px;
    letter-spacing: 0.5px;
    color: var(--ink-white);
  }
  .front-url .front-url__domain { color: var(--accent-bright); }

  .holder-name {
    position: absolute;
    left: 60px;
    top: 48px;
    font-weight: 600;
    font-size: 24px;
    letter-spacing: 1.5px;
    text-transform: uppercase;
  }
  .divider {
    position: absolute;
    left: 48px;
    right: 40px;
    top: 100px;
    height: 3px;
    background: var(--accent-bright);
  }
  .card--back .brand {
    right: 60px;
    top: 160px;
  }
  .brand__name--small { font-size: 30px; }

  .contact-list {
    position: absolute;
    right: 60px;
    bottom: 38px;
    list-style: none;
    text-align: right;
  }
  .contact-list__item {
    display: flex;
    align-items: center;
    justify-content: flex-end;
    gap: 12px;
    font-size: 19px;
    line-height: 30px;
    color: var(--ink-white);
  }
  .contact-list__icon {
    width: 18px;
    height: 18px;
    flex: none;
  }
</style>
</head>
<body>
  <main class="sheet">

    <section class="card card--front" aria-label="Business card front">
      <div class="pattern-field" role="img" aria-label="Subtle curved grid of squares decorating the card corner"></div>
      <div class="brand">
        <span class="brand__dot"></span>
        <span class="brand__name">Tidewell Event Group</span>
      </div>
      <p class="front-url">www.<span class="front-url__domain">tidewell</span>.com</p>
    </section>

    <section class="card card--back" aria-label="Business card back">
      <div class="pattern-field" role="img" aria-label="Subtle curved grid of squares decorating the card edge"></div>
      <h1 class="holder-name">Owen Marlow</h1>
      <div class="divider"></div>
      <div class="brand">
        <span class="brand__dot"></span>
        <span class="brand__name brand__name--small">Tidewell Event Group</span>
      </div>
      <ul class="contact-list">
        <li class="contact-list__item">
          0000 512 748
          <svg class="contact-list__icon" viewBox="0 0 24 24" aria-hidden="true">
            <path fill="#0791cd" d="M6.6 10.8a15.1 15.1 0 0 0 6.6 6.6l2.2-2.2a1 1 0 0 1 1-.25 11.4 11.4 0 0 0 3.6.57 1 1 0 0 1 1 1V20a1 1 0 0 1-1 1A17 17 0 0 1 3 4a1 1 0 0 1 1-1h3.5a1 1 0 0 1 1 1c0 1.25.2 2.45.57 3.6a1 1 0 0 1-.25 1z"/>
          </svg>
        </li>
        <li class="contact-list__item">
          hello@tidewell.com
          <svg class="contact-list__icon" viewBox="0 0 24 24" aria-hidden="true">
            <rect x="2" y="5" width="20" height="14" rx="1.5" fill="#0791cd"/>
            <path d="M3 6.5l9 6.5 9-6.5" fill="none" stroke="#0a2f5e" stroke-width="1.6"/>
          </svg>
        </li>
        <li class="contact-list__item">
          www.tidewell.com
          <svg class="contact-list__icon" viewBox="0 0 24 24" aria-hidden="true">
            <circle cx="12" cy="12" r="10" fill="#0791cd"/>
            <g fill="none" stroke="#0a2f5e" stroke-width="1.4">
              <ellipse cx="12" cy="12" rx="4.2" ry="10"/>
              <line x1="2" y1="12" x2="22" y2="12"/>
              <path d="M4 7h16M4 17h16"/>
            </g>
          </svg>
        </li>
      </ul>
    </section>

  </main>
</body>
</html>
```